Letterhead for a German Distribution/Manufacturing Company

We need a professional Letterhead in a unique Design.
not to playful.
The Letterhead has to show show that we are a international company with headquater in Nordland.
all details like adress, Vat Tax Number, Bank Accout, Eori, email, Company number has to be on the Letterhead.
for example use: VAT TAX DE5704168 Bank Account: Norrfeld Bank IBAN DE421705238ß310482 Swift: KOLV3154802 EORI 3041296587 Company Number: HRB 61508 Adress: VOLTRINA UG Amsel Strasse 7 Postal Code 04683 City Halvenstadt Country: Nordland Email: info@voltrina-example.com
the design can be colored but doesnt have to be
Industry/Entity Type
Manufacturing and international distribution
Requirements
Must have
- show that we are a international company with headquater in Nordland. our company infos and logo

```html
<!DOCTYPE html>
<html lang="en">
<head>
<meta charset="utf-8">
<title>Voltrina Letterhead</title>
<link href="https://fonts.googleapis.com/css2?family=Roboto:wght@400;500;700&display=swap" rel="stylesheet">
<style>
  :root {
    --backdrop: #e9e8e9;
    --paper: #ffffff;
    --ink: #141414;
    --watermark: #f4f4f4;
    --sign-ink: #d8d8d8;
  }
  * { margin: 0; padding: 0; box-sizing: border-box; }
  html, body { width: 1200px; height: 752px; overflow: hidden; }
  body {
    background: var(--backdrop);
    font-family: "Roboto", Arial, sans-serif;
    color: var(--ink);
    position: relative;
  }
  .sheet {
    position: absolute;
    top: 67px;
    width: 437px;
    height: 617px;
    background: var(--paper);
    box-shadow: 0 3px 8px rgba(0,0,0,0.35);
    overflow: hidden;
  }
  .sheet--blank { left: 109px; }
  .sheet--letter { left: 654px; }

  .watermark {
    position: absolute;
    left: 123px;
    top: 156px;
    width: 268px;
    height: 268px;
    border-radius: 50%;
    background: var(--watermark);
  }

  .brand {
    position: absolute;
    left: 27px;
    top: 28px;
    display: flex;
    align-items: center;
    gap: 6px;
  }
  .brand__dot {
    width: 22px;
    height: 22px;
    border-radius: 50%;
    background: var(--ink);
  }
  .brand__name {
    font-size: 18px;
    font-weight: 400;
    letter-spacing: 0.3px;
    line-height: 1;
  }

  .contact {
    position: absolute;
    right: 32px;
    top: 34px;
    text-align: right;
    font-size: 6.8px;
    line-height: 9px;
  }
  .label { font-weight: 700; }

  .footer {
    position: absolute;
    left: 31px;
    right: 31px;
    top: 568px;
    font-size: 6.6px;
    line-height: 9px;
    display: flex;
    justify-content: space-between;
    align-items: flex-start;
  }
  .footer__col--address { text-align: left; margin-top: 1px; }
  .footer__col--bank { text-align: center; margin-top: 1px; margin-left: 20px; }
  .footer__col--registry { text-align: right; margin-top: -1px; }

  .letter {
    position: absolute;
    left: 52px;
    top: 134px;
    font-size: 7.6px;
    line-height: 10px;
    white-space: nowrap;
  }
  .letter__recipient { font-weight: 500; }
  .letter__subject { margin-top: 10px; }
  .letter__para { margin-top: 20px; }
  .letter__para + .letter__para { margin-top: 20px; }
  .letter__closing { margin-top: 20px; }
  .signature {
    margin-top: 8px;
    width: 73px;
    height: 16px;
    background: var(--sign-ink);
    border-radius: 3px;
  }
</style>
</head>
<body>

  <section class="sheet sheet--blank">
    <div class="watermark" aria-hidden="true"></div>
    <div class="brand">
      <span class="brand__dot"></span>
      <span class="brand__name">VOLTRINA</span>
    </div>
    <div class="contact">
      <div><span class="label">Email:</span> info@voltrina-example.com</div>
      <div><span class="label">Website:</span> www.voltrina-example.com</div>
    </div>
    <footer class="footer">
      <div class="footer__col footer__col--address">
        <div><span class="label">Adress:</span> VOLTRINA UG</div>
        <div>Amsel Strasse 7, 04683,</div>
        <div>Halvenstadt, Nordland</div>
      </div>
      <div class="footer__col footer__col--bank">
        <div><span class="label">VAT</span> TAX DE5704168</div>
        <div><span class="label">Bank Account:</span> Norrfeld Bank</div>
        <div><span class="label">IBAN</span> DE421705238ß310482</div>
      </div>
      <div class="footer__col footer__col--registry">
        <div><span class="label">Swift:</span> KOLV3154802</div>
        <div><span class="label">EORI</span> 3041296587</div>
        <div><span class="label">Company Number:</span> HRB 61508</div>
      </div>
    </footer>
  </section>

  <section class="sheet sheet--letter">
    <div class="watermark" aria-hidden="true"></div>
    <div class="brand">
      <span class="brand__dot"></span>
      <span class="brand__name">VOLTRINA</span>
    </div>
    <div class="contact">
      <div><span class="label">Email:</span> info@voltrina-example.com</div>
      <div><span class="label">Website:</span> www.voltrina-example.com</div>
    </div>

    <article class="letter">
      <div class="letter__recipient">
        <div>To,</div>
        <div>Chairman</div>
        <div>Voltrina Group</div>
        <div>Nordland</div>
      </div>
      <p class="letter__subject"><span class="label">Sub:</span> Lorem ipsum dolor sit amet, consectetuer adipiscing elit.</p>
      <p class="letter__para">
        Lorem ipsum dolor sit amet, consectetuer adipiscing elit, sed diam nonummy nibh<br>
        euismod tincidunt ut laoreet dolore magna aliquam erat volutpat. Ut wisi enim ad minim<br>
        veniam, quis nostrud exerci tation ullamcorper suscipit.
      </p>
      <p class="letter__para">
        Lorem ipsum dolor sit amet, cons ectetuer adipiscing elit, sed diam nonummy nibh<br>
        euismod tincidunt ut laoreet dolore magna.
      </p>
      <p class="letter__closing">Regards</p>
      <div class="signature" role="img" aria-label="Handwritten signature of the sender"></div>
    </article>

    <footer class="footer">
      <div class="footer__col footer__col--address">
        <div><span class="label">Adress:</span> VOLTRINA UG</div>
        <div>Amsel Strasse 7, 04683,</div>
        <div>Halvenstadt, Nordland</div>
      </div>
      <div class="footer__col footer__col--bank">
        <div><span class="label">VAT</span> TAX DE5704168</div>
        <div><span class="label">Bank Account:</span> Norrfeld Bank</div>
        <div><span class="label">IBAN</span> DE421705238ß310482</div>
      </div>
      <div class="footer__col footer__col--registry">
        <div><span class="label">Swift:</span> KOLV3154802</div>
        <div><span class="label">EORI</span> 3041296587</div>
        <div><span class="label">Company Number:</span> HRB 61508</div>
      </div>
    </footer>
  </section>

</body>
</html>
```